Varnel Group Business Card design with current logo

hello all , we have abranded logo which i will attach but we need a card double sided designed . one side is easy as its the logo but the other side we want clean and modern. The info needed will be the same text as the card sample attached. no pictures of us though just clean and professinal pls. Logo can be incorporated on the text side to for recognition. Colors are Black , white , red and grey... ideal card would be matt finish high end stock. or a black card so white text ... Sorry i have uploaded al the files i got when I had the logo designed on here.. Oh forgot want to say pls add in the card details EST 1981 and over 40yrs combined experiance
Updates

Hello everyone , I'm really sorry we haven't been able to make a final decision.. There is at least 3 cards that all have there positives over the other two... We will decide by tonight.

Target Market(s)

20-70 wide range but people with money and a education.

Industry/Entity Type

Real Estate Agent

Contact Information for Business Card

One side the Logo choose from the different color logos, black being the one we like most, other side is the details. Clean professional looking fonts. EST 1981 , over 40yrs experiance. Website email and both names and PH# as per the sample card attached

Font styles to use
Other font styles liked:
• Fonts:Code Bold,Code Light, Lucida Fax.

Colors
1b1b1b
757575
c9c9c9
e8e8e8
ffffff
e9e9e9

Requirements
Must have
• Logo and contact info

```html
<!DOCTYPE html>
<html lang="en">
<head>
<meta charset="utf-8">
<title>Varnel Group Business Card</title>
<link rel="stylesheet" href="https://fonts.googleapis.com/css2?family=Arimo:wght@400&family=Noto+Serif:ital,wght@0,400;1,400&display=swap">
<style>
  :root {
    --page-bg: #2e2b29;
    --card-bg: #1e1e1e;
    --mark-bg: #0c0c0c;
    --white: #ffffff;
    --light-grey: #e8e8e8;
    --mid-grey: #c9c9c9;
    --dark-grey: #757575;
    --accent-red: #c4141b;
  }
  * { box-sizing: border-box; margin: 0; padding: 0; }
  html, body {
    width: 1200px; height: 886px; overflow: hidden;
    background: var(--page-bg);
  }
  .stage {
    position: relative; width: 1200px; height: 886px;
  }
  .card {
    position: absolute; width: 540px; height: 309px;
    background: var(--card-bg);
    box-shadow: 0 10px 30px rgba(0,0,0,.45);
  }
  .card--front { left: 40px; top: 288px; }
  .card--back  { left: 620px; top: 288px; }

  .brand {
    position: absolute; display: flex; align-items: center; gap: 12px;
  }
  .brand__square {
    width: 46px; height: 46px; background: var(--mark-bg);
  }
  .brand__name {
    font-family: "Arimo", sans-serif; font-weight: 400;
    font-size: 26px; letter-spacing: 1px; color: var(--white);
    line-height: 1;
  }
  .card--front .brand { left: 150px; top: 118px; }
  .established {
    position: absolute; left: 150px; top: 214px;
    font-family: "Arimo", sans-serif; font-size: 13px;
    letter-spacing: 2px; color: var(--mid-grey);
  }

  .card--back .brand { left: 28px; top: 92px; }
  .card--back .brand__name { font-size: 20px; }
  .card--back .brand__square { width: 38px; height: 38px; }
  .tagline {
    position: absolute; left: 30px; bottom: 30px;
    font-family: "Noto Serif", serif; font-style: italic;
    font-size: 13px; color: var(--light-grey);
  }

  .details {
    position: absolute; left: 292px; top: 34px; width: 236px;
    font-family: "Noto Serif", serif; color: var(--light-grey);
  }
  .details__names {
    font-size: 17px; line-height: 1.2; color: var(--white); margin-bottom: 12px;
  }
  .contact-list { list-style: none; font-size: 12.5px; line-height: 1.55; }
  .contact-list li { display: flex; align-items: center; gap: 8px; }
  .contact-list svg { width: 10px; height: 10px; flex: none; }

  .office {
    display: flex; align-items: center; gap: 10px; margin-top: 14px;
    font-size: 12.5px; line-height: 1.3;
  }
  .office__badge {
    width: 34px; height: 26px; background: var(--white); flex: none;
  }
  .address {
    display: flex; gap: 8px; margin-top: 10px;
    font-size: 12.5px; line-height: 1.3;
  }
  .address svg { width: 10px; height: 13px; flex: none; margin-top: 2px; }
</style>
</head>
<body>
<main class="stage">

  <section class="card card--front" aria-label="Card front">
    <div class="brand">
      <span class="brand__square"></span>
      <span class="brand__name">VARNEL GROUP</span>
    </div>
    <p class="established">EST 1981</p>
  </section>

  <section class="card card--back" aria-label="Card back">
    <div class="brand">
      <span class="brand__square"></span>
      <span class="brand__name">VARNEL GROUP</span>
    </div>
    <p class="tagline">Over 40yrs Combined Experiance</p>

    <div class="details">
      <p class="details__names">Dale Varnel<br>Jesse Varnel</p>
      <ul class="contact-list">
        <li>
          <svg viewBox="0 0 10 10"><rect x="2.5" y="0.5" width="5" height="9" rx="1" fill="none" stroke="var(--accent-red)" stroke-width="1.2"/></svg>
          250-555-0133
        </li>
        <li>
          <svg viewBox="0 0 10 10"><rect x="1" y="1" width="8" height="8" rx="1" fill="none" stroke="var(--accent-red)" stroke-width="1.2"/><path d="M3 3.5h4M3 6h4" stroke="var(--accent-red)" stroke-width="1"/></svg>
          250-555-0165
        </li>
        <li>
          <svg viewBox="0 0 10 10"><rect x="0.5" y="2" width="9" height="6.5" fill="var(--accent-red)"/><path d="M0.5 2l4.5 3.5L9.5 2" fill="none" stroke="var(--card-bg)" stroke-width="0.9"/></svg>
          info@varnelrealty.com
        </li>
        <li>
          <svg viewBox="0 0 10 10"><circle cx="5" cy="5" r="4" fill="none" stroke="var(--accent-red)" stroke-width="1.2"/><path d="M1 5h8M5 1c-2 2.5-2 5.5 0 8M5 1c2 2.5 2 5.5 0 8" fill="none" stroke="var(--accent-red)" stroke-width="0.8"/></svg>
          www.varnelrealty.com
        </li>
      </ul>

      <div class="office">
        <span class="office__badge"></span>
        <span>Harbourline<br>Realty West</span>
      </div>

      <div class="address">
        <svg viewBox="0 0 10 13"><path d="M5 0.5a4 4 0 0 1 4 4c0 3-4 8-4 8s-4-5-4-8a4 4 0 0 1 4-4z" fill="var(--accent-red)"/><circle cx="5" cy="4.5" r="1.5" fill="var(--card-bg)"/></svg>
        <span>210-1850 Kestrel Way<br>Victoria BC V8Z 4M1</span>
      </div>
    </div>
  </section>

</main>
</body>
</html>
```